Wordpress Design Project

We need a wordpress design for a new creative innovation company based in Melbourne called Quillbarrow.
We develop innovative growth and communication strategies for our clients who are generally medium sized businesses wanting to find new ways to grow their businesses.
Our Services include:
Business Strategy
Communications and Strategic Planning
Creative Consultancy
Professional Development
Change Management
Project Management
We would like our wordpress design to be simple and professional yet give a feeling of innovation, kind of like old meeting new.
We are leaning towards the predominant background colour being white, but open to suggestions.
Attached are logo files.
If you require any further information please contact us via the Marble Yard site.

```html
<!DOCTYPE html>
<html lang="en">
<head>
<meta charset="utf-8">
<title>Quillbarrow</title>
<link rel="stylesheet" href="https://fonts.googleapis.com/css2?family=Source+Sans+3:wght@400;600&family=Roboto+Condensed:wght@400&family=Open+Sans:wght@400&family=Noto+Sans:wght@400&display=swap">
<style>
:root{
  --green:#8cc63f;
  --green-dark:#5f9f22;
  --green-text:#6aab2b;
  --slate:#5b6470;
  --ink:#555a60;
  --body-text:#5e6166;
  --rule:#d6d6d6;
  --footer:#474747;
  --footer-bottom:#333333;
  --footer-text:#e2e2e2;
}
*{margin:0;padding:0;box-sizing:border-box}
html,body{width:1200px;height:1148px;overflow:hidden;background:#fff}
body{position:relative;font-family:"Source Sans 3",sans-serif;color:var(--body-text)}
.abs{position:absolute}
.top-strip{left:0;top:0;width:1200px;height:14px;background:var(--slate)}
.backdrop{left:0;top:153px;width:1200px;height:330px;background:linear-gradient(#f1f1f1,#fff)}
.brand{left:100px;top:48px;display:flex;align-items:center;gap:10px;font-family:"Source Sans 3",sans-serif;font-weight:400;font-size:50px;color:var(--green);letter-spacing:-1px}
.brand-dot{width:26px;height:26px;border-radius:50%;background:var(--green)}
.social{left:971px;top:70px;display:flex;gap:8px}
.social span{width:27px;height:27px;border-radius:50%;background:var(--green);display:flex;align-items:center;justify-content:center}
.nav{left:100px;top:134px;width:1002px;height:39px;border-radius:14px 14px 0 0;background:linear-gradient(#b4e07c,#86c443);display:flex;align-items:stretch;font-family:"Noto Sans",sans-serif;font-size:13.5px;color:#1d2a10}
.nav a{color:inherit;text-decoration:none;display:flex;align-items:center;padding:0 21px;border-right:1px solid rgba(70,120,20,.45);box-shadow:1px 0 0 rgba(255,255,255,.35)}
.nav .home{width:63px;justify-content:center;padding:0;background:linear-gradient(#8ccb45,#5fa922);border-radius:14px 0 0 0}
.search{left:885px;top:142px;width:198px;height:25px;border-radius:12px;background:#fff;border:1px solid #7a9d58;box-shadow:inset 0 1px 2px rgba(0,0,0,.25)}
.search svg{position:absolute;right:7px;top:4px}
.hero{left:101px;top:173px;width:1000px;height:297px;border:1px solid #b8bcc2;border-top:0;background:linear-gradient(90deg,#2a3140 0%,#5d6b80 22%,#b6c8d8 45%,#dbe6ef 70%,#f3f6f8 100%);overflow:hidden}
.hero-shadow{left:70px;top:468px;width:1062px;height:14px;background:radial-gradient(ellipse at center top,rgba(0,0,0,.35),rgba(0,0,0,0) 70%)}
.hero-caption{left:733px;top:364px;color:#3e4248;font-family:"Source Sans 3",sans-serif}
.hero-caption .lead{font-size:23px;line-height:28px}
.hero-caption .main{font-size:35px;line-height:44px}
.pager{left:500px;top:433px;width:220px;height:38px;background:linear-gradient(#5a5a5a,#1f1f1f);border-radius:12px 12px 0 0;clip-path:polygon(6% 0,92% 0,100% 100%,0 100%);display:flex;justify-content:center;align-items:center;gap:15px;padding-bottom:2px}
.pager i{width:13px;height:13px;border-radius:50%;background:#222;box-shadow:inset 0 1px 2px #000,0 1px 0 rgba(255,255,255,.2)}
.pager i.on{background:#f2f2f2}
.welcome-title{left:101px;top:514px;font-family:"Open Sans",sans-serif;font-size:26px;color:var(--green);letter-spacing:.3px}
.welcome-text{left:101px;top:559px;width:704px;font-size:12.6px;line-height:23px;text-align:justify}
.welcome-photo{left:821px;top:518px;width:276px;height:146px;border:3px solid #dedede;border-radius:5px;background:#fff;padding:1px}
.welcome-photo div{width:100%;height:100%;background:linear-gradient(90deg,#cfd4da,#eceff2 55%,#f6f3ef)}
.divider{left:101px;top:699px;width:1001px;height:1px;background:var(--rule)}
.col{top:722px;width:303px}
.col-rule{top:722px;width:1px;height:174px;background:var(--rule)}
.col h2{display:flex;align-items:flex-end;gap:9px;height:42px;font-family:"Roboto Condensed",sans-serif;font-weight:400;font-size:23.5px;color:var(--green-text);text-transform:uppercase}
.col h2 .icon{width:32px;height:40px;border-radius:4px;background:linear-gradient(#7f8a98,#3f4a58)}
.col p{margin-top:15px;font-size:12.6px;line-height:23px;text-align:justify}
.col .more{display:flex;align-items:center;gap:6px;margin-top:16px;font-size:12.5px;color:var(--green-text);text-decoration:none;text-transform:uppercase}
.quote{font-family:Georgia,serif;font-size:22px;color:#555;line-height:0;vertical-align:-6px;margin:0 8px 0 0}
.footer{left:0;top:937px;width:1200px;height:167px;background:var(--footer);color:var(--footer-text)}
.footer-bottom{left:0;top:1104px;width:1200px;height:44px;background:var(--footer-bottom);color:#bdbdbd;font-size:12.5px;display:flex;align-items:center;justify-content:center}
.footer h3{position:absolute;font-weight:400;font-size:12px}
.links{position:absolute;top:52px;list-style:none;font-size:12.6px}
.links li{height:26px;padding-left:16px;position:relative}
.links li::before{content:"";position:absolute;left:1px;top:7px;width:4px;height:4px;border-radius:50%;background:#aaa}
.contact{position:absolute;left:863px;top:54px;font-size:12.6px;line-height:24px}
</style>
</head>
<body>
<div class="abs top-strip"></div>
<div class="abs backdrop"></div>

<header>
  <div class="abs brand"><span>Quillbarrow</span><span class="brand-dot"></span></div>
  <div class="abs social" aria-label="Social links">
    <span></span><span></span><span></span>
    <span><svg width="15" height="11" viewBox="0 0 15 11"><rect x="0.75" y="0.75" width="13.5" height="9.5" fill="none" stroke="#fff" stroke-width="1.5"/><path d="M1 1 7.5 6 14 1" fill="none" stroke="#fff" stroke-width="1.5"/></svg></span>
  </div>
</header>

<nav class="abs nav">
  <a class="home" href="#" aria-label="Home"><svg width="16" height="14" viewBox="0 0 16 14"><path d="M8 0 16 7h-2.5v7H10V9.5H6V14H2.5V7H0z" fill="#fff"/></svg></a>
  <a href="#">About us</a>
  <a href="#">Services</a>
  <a href="#">Testimonials</a>
  <a href="#">Blogs</a>
  <a href="#">Contact us</a>
</nav>
<div class="abs search"><svg width="15" height="15" viewBox="0 0 15 15"><circle cx="6" cy="6" r="4.5" fill="none" stroke="#555" stroke-width="1.4"/><path d="M9.3 9.3 14 14" stroke="#555" stroke-width="1.8"/></svg></div>

<section>
  <div class="abs hero" role="img" aria-label="Smiling businesswoman beside a hand touching glowing interface tiles"></div>
  <div class="abs hero-shadow"></div>
  <div class="abs hero-caption">
    <div class="lead">Vivamus feugiat egestas lacus,</div>
    <div class="main">vitae pulvinar tellus</div>
  </div>
  <div class="abs pager"><i class="on"></i><i></i><i></i><i></i></div>
</section>

<section>
  <h1 class="abs welcome-title" style="font-weight:400">Welcome to our site</h1>
  <p class="abs welcome-text">Sed ut perspiciatis unde omnis iste natus error sit voluptatem accusantium doloremque laudantium, totam rem aperiam, eaque ipsa quae ab illo inventore veritatis et quasi architecto beatae vitae dicta sunt explicabo. Nemo enim ipsam voluptatem quia voluptas sit aspernatur aut odit aut fugit, sed quia consequuntur magni dolores eos qui ratione voluptatem sequi nesciunt. Neque porro quisquam est, qui dolorem ipsum quia dolor sit amet, consectetur, adipisci velit, sed quia non numquam eius modi tempora incidunt ut labore et dolore magnam aliquam quaerat.</p>
  <div class="abs welcome-photo"><div role="img" aria-label="Cheerful office team celebrating with a woman giving a thumbs up"></div></div>
</section>

<div class="abs divider"></div>

<section>
  <div class="abs col" style="left:101px">
    <h2><span class="icon" role="img" aria-label="Businessman icon"></span>About us</h2>
    <p>Nemo enim ipsam voluptatem quia voluptas sit aspernatur aut odit aut fugit, sed quia consequuntur magni dolores eos qui ratione voluptatem sequi nesciunt. Neque porro quisquam est.</p>
    <a class="more" href="#">View more <svg width="6" height="9" viewBox="0 0 6 9"><path d="M0 0 6 4.5 0 9z" fill="#6aab2b"/></svg></a>
  </div>
  <div class="abs col-rule" style="left:426px"></div>
  <div class="abs col" style="left:451px">
    <h2><span class="icon" role="img" aria-label="Gear icon" style="border-radius:50%;height:38px;width:38px"></span>Our services</h2>
    <p>Nemo enim ipsam voluptatem quia voluptas sit aspernatur aut odit aut fugit, sed quia consequuntur magni dolores eos qui ratione voluptatem sequi nesciunt. Neque porro quisquam est.</p>
    <a class="more" href="#">View more <svg width="6" height="9" viewBox="0 0 6 9"><path d="M0 0 6 4.5 0 9z" fill="#6aab2b"/></svg></a>
  </div>
  <div class="abs col-rule" style="left:775px"></div>
  <div class="abs col" style="left:799px">
    <h2><svg width="34" height="28" viewBox="0 0 34 28" aria-hidden="true"><path d="M5 2h24a4 4 0 0 1 4 4v10a4 4 0 0 1-4 4H14l-7 6 1-6H5a4 4 0 0 1-4-4V6a4 4 0 0 1 4-4z" fill="#e7e7e7" stroke="#a8a8a8"/></svg>Testimonials</h2>
    <p><span class="quote">“</span>Nemo enim ipsam voluptatem quia voluptas sit aspernatur aut odit aut fugit, sed quia consequuntur magni dolores eos qui ratione voluptatem sequi nesciunt. Neque porro quisquam est. <span class="quote" style="margin:0 0 0 8px">”</span></p>
    <a class="more" href="#">View more <svg width="6" height="9" viewBox="0 0 6 9"><path d="M0 0 6 4.5 0 9z" fill="#6aab2b"/></svg></a>
  </div>
</section>

<footer>
  <div class="abs footer">
    <h3 style="left:101px;top:22px">Quick Links</h3>
    <ul class="links" style="left:101px"><li>Footer Link 1</li><li>Footer Link 2</li><li>Footer Link 3</li><li>Footer Link 4</li></ul>
    <ul class="links" style="left:237px"><li>Footer Link 1</li><li>Footer Link 2</li><li>Footer Link 3</li><li>Footer Link 4</li></ul>
    <ul class="links" style="left:373px"><li>Footer Link 1</li><li>Footer Link 2</li><li>Footer Link 3</li><li>Footer Link 4</li></ul>
    <ul class="links" style="left:508px"><li>Footer Link 1</li><li>Footer Link 2</li><li>Footer Link 3</li><li>Footer Link 4</li></ul>
    <ul class="links" style="left:654px"><li>Footer Link 1</li><li>Footer Link 2</li></ul>
    <h3 style="left:863px;top:24px">Contact us</h3>
    <div class="contact">
      <div>Quillbarrow</div>
      <div>Vel illum qui dolorem, contantry&nbsp; - &nbsp;DC008</div>
      <div>Ph : +61 3 5550 1820</div>
      <div>EM : info@quillbarrow.com</div>
    </div>
  </div>
  <div class="abs footer-bottom">Copyright © 2012 Quillbarrow. All rights reserved.</div>
</footer>
</body>
</html>
```